New Company Newsletter Template Needed!!!

We need some new graphics/design for us to create our company newsletter in MS Publisher/Word. Prefer simple, modern design that can be easy to update each month, flexible for adding images and include our company logo (attached).
Also attached our basic existing template but we do not want to use the same “swoosh” ribbon and want to reduce the number of colours used.
Needs to be elements we can move into the software and create a PDF newsletter to circulate.

Font styles to use
Sans Serif

Requirements
Must have
• Company logo
Nice to have
• If any colours should fit into our company logo palette

```html
<!DOCTYPE html>
<html lang="en">
<head>
<meta charset="utf-8">
<title>Brightwell Newsletter – Issue 01</title>
<link rel="stylesheet" href="https://fonts.googleapis.com/css2?family=Source+Sans+3:ital,wght@0,400;0,600;0,700;1,400&display=swap">
<style>
  :root {
    --navy: #253a7d;
    --sky: #1b9ad6;
    --sky-soft: #bfe6fa;
    --sky-mid: #6cc6f2;
    --band-blue: #1a9fdb;
    --panel-grey: #5a5b5f;
    --photo-grey: #dcdcde;
    --ink: #231f20;
    --frame: #b9b9b9;
    --paper: #ffffff;
    --accent-red: #c8102e;
    --accent-orange: #e8501e;
    --accent-yellow: #ffd100;
  }
  * { box-sizing: border-box; margin: 0; padding: 0; }
  html, body { width: 966px; height: 1200px; overflow: hidden; background: var(--paper); }
  body { font-family: "Source Sans 3", sans-serif; color: var(--ink); position: relative; }

  .page-frame {
    position: absolute; left: 48px; top: 36px; width: 877px; height: 1135px;
    border: 1px solid var(--frame); overflow: hidden; background: var(--paper);
  }

  .header-backdrop {
    position: absolute; left: 0; top: 0; width: 100%; height: 290px;
    background:
      linear-gradient(180deg, rgba(255,255,255,0) 60%, var(--paper) 100%),
      linear-gradient(90deg, #eef8fe 0%, var(--sky-soft) 45%, var(--sky-mid) 100%);
  }
  .footer-backdrop {
    position: absolute; left: 0; bottom: 0; width: 100%; height: 70px;
    background:
      linear-gradient(0deg, rgba(255,255,255,0) 0%, rgba(255,255,255,0) 40%, var(--paper) 100%),
      linear-gradient(90deg, #f4fbff 0%, var(--sky-soft) 60%, var(--sky-mid) 100%);
  }

  .masthead-title {
    position: absolute; left: 54px; top: 34px;
    font-weight: 700; font-size: 100px; line-height: 1; letter-spacing: -2px;
    color: var(--navy); z-index: 2;
  }
  .issue-bar {
    position: absolute; left: 57px; top: 119px; width: 432px; height: 38px;
    background: var(--navy); color: #fff; z-index: 1;
    font-style: italic; font-size: 19px; letter-spacing: 0.5px;
    padding: 6px 12px; line-height: 26px;
  }
  .issue-rule {
    position: absolute; left: 57px; top: 157px; width: 432px; height: 5px;
    background: linear-gradient(90deg, var(--accent-red), var(--accent-orange) 55%, var(--accent-yellow));
  }

  .brand {
    position: absolute; left: 632px; top: 36px;
    display: flex; align-items: center; gap: 10px;
  }
  .brand-square { width: 44px; height: 44px; background: var(--accent-red); }
  .brand-name { font-size: 38px; font-weight: 600; color: var(--navy); letter-spacing: -0.5px; }

  .lead-article { position: absolute; left: 46px; top: 318px; width: 374px; }
  .lead-heading { font-size: 31px; font-weight: 700; color: var(--sky); line-height: 1.2; margin-bottom: 4px; }
  .lead-article p, .ceo-message p {
    font-size: 16px; line-height: 20.8px; text-transform: uppercase;
    text-align: justify; margin-bottom: 20.8px;
  }

  .ceo-card { position: absolute; left: 487px; top: 314px; width: 342px; }
  .ceo-photo { height: 276px; background: var(--photo-grey); }
  .ceo-band {
    height: 70px; background: var(--band-blue); color: var(--navy);
    font-size: 25px; font-weight: 700; text-align: center; line-height: 70px;
  }
  .ceo-message { background: var(--panel-grey); color: #fff; padding: 18px 24px 10px; height: 384px; }

  .footer-note { position: absolute; left: 28px; bottom: 16px; font-size: 13px; color: var(--navy); }
</style>
</head>
<body>
  <div class="page-frame">
    <div class="header-backdrop" role="img" aria-label="Soft blue header background"></div>
    <div class="footer-backdrop" role="img" aria-label="Soft blue footer background"></div>

    <div class="issue-bar">ISSUE : 01 &nbsp;|&nbsp; MAY 2020</div>
    <div class="issue-rule"></div>
    <h1 class="masthead-title">Newsletter</h1>

    <div class="brand">
      <span class="brand-square"></span>
      <span class="brand-name">Brightwell</span>
    </div>

    <article class="lead-article">
      <h2 class="lead-heading">BRIGHTWELL.....</h2>
      <p>Lorem ipsum dolor sit amet, consectetuer adipiscing elit. Aenean commodo ligula eget dolor. Aenean</p>
      <p>Massa. Cum sociis natoque penatibus et magnis dis parturient monies, nascetur ridiculus mus. Donec ohm felts, ultricies nec, pellentesque eu, pretium</p>
      <p>Quis, sem. Nulla consequat massa quis enim. Donec pede justo, fringilla vel, aliquet nec, vulputate eget, arcu. In enim justo, rhoncus ut, imperdiet a, venenatis vitae, justo. Nullam dictum</p>
      <p>Felts eu pede mollis pretium. Integer tincidunt. Gras dapibus. Vivamus elementum semper nisi. Aenean vulputate eleifend tellus. Aenean leo ligula, porttitor eu, consequat vitae, eleifend ac, enim. Aliquam lorem ante, dapibus in, viverra quis, feugiat a, tellus. Phasellus viverra nulla ut metus varius laoreet. Quisque rutrum. Aenean imperdiet. Etiam ultricies nisi vel augue. Curabitur ullamcorper ultricies nisi. Nam eget dui. Etiam</p>
      <p>Quis, sem. Nulla consequat massa quis enim. Donec pede justo, fringilla vel, aliquet nec, vulputate eget, arcu. In enim justo, rhoncus ut, imperdiet a, venenatis vitae, justo. Nullam dictum</p>
    </article>

    <aside class="ceo-card">
      <div class="ceo-photo" role="img" aria-label="Portrait photo of the CEO"></div>
      <div class="ceo-band">Message From Your CEO</div>
      <div class="ceo-message">
        <p>Lorem ipsum dolor sit amet, consectetuer adipiscing elit. Aenean commodo ligula eget dolor. Aenean</p>
        <p>Massa. Cum sociis natoque penatibus et magnis dis parturient monies, nascetur ridiculus mus. Donec ohm felts, ultricies nec, pellentesque eu, pretium</p>
        <p>Quis, sem. Nulla consequat massa quis enim. Donec pede justo, fringilla vel, aliquet nec, vulputate eget, arcu. In enim justo, rhoncus ut, imperdiet a, venenatis vitae, justo. Nullam dictum</p>
      </div>
    </aside>

    <p class="footer-note">for internal use within the brightwell group only</p>
  </div>
</body>
</html>
```